We need a business card design for our website qvwtrading.net. The Star Headline is qvwtrading.net, in large lettering.We sell fashion rings of titanium, mirror pollished stainless steel, and related jewelry. Basically quality products competing with the high expense of gold.We have to portray honesty and trust, because thats who I am. I know marketing, but I am weak on colors and layout. 3D Gold curved edge letters are ok. No green and yellow.Black,Red,Purple and White in small amounts.No fancy Lettering.
No Rainbows in printing.
Our goal is selling our products online globally

Kind Regards Maren Tulloch

Fashion

qvwtrading.net
known for our ideal fit rings
email.marentullochptyltd@corvexmail com

```html
<!DOCTYPE html>
<html lang="en">
<head>
<meta charset="utf-8">
<title>Qvwtrading.net – Business Card</title>
<link rel="stylesheet" href="https://fonts.googleapis.com/css2?family=Tinos&family=Arimo:wght@400;700&display=swap">
<style>
  :root {
    --page-bg: #e9e9e9;
    --card-white: #ffffff;
    --card-shade: #dcdcdc;
    --gold-deep: #a8720f;
    --gold-mid: #d9a231;
    --gold-light: #f3cf6a;
    --gold-pale: #f1e2a6;
    --gold-text: #b39a55;
    --ink: #1e1e1e;
    --band-text: #ffffff;
    --ring-tone-dark: #9a9a9a;
    --ring-tone-light: #f2f2f2;
  }
  * { margin: 0; padding: 0; box-sizing: border-box; }
  html, body {
    width: 1200px;
    height: 900px;
    overflow: hidden;
    background: var(--page-bg);
  }
  .canvas {
    position: relative;
    width: 1200px;
    height: 900px;
  }
  .card {
    position: absolute;
    left: 320px;
    width: 560px;
    height: 330px;
    border-radius: 18px;
    overflow: hidden;
    background: radial-gradient(ellipse at 50% 40%, var(--card-white) 0%, #f4f4f4 45%, var(--card-shade) 100%);
    box-shadow: 0 8px 22px rgba(0,0,0,0.18);
  }
  .card--back { top: 90px; }
  .card--front { top: 470px; }

  .gold-band {
    position: absolute;
    left: 0;
    right: 0;
    bottom: 0;
    background: linear-gradient(90deg, var(--gold-deep) 0%, var(--gold-mid) 30%, var(--gold-light) 55%, var(--gold-mid) 78%, var(--gold-deep) 100%);
  }
  .gold-band::before {
    content: "";
    position: absolute;
    left: 0;
    right: 0;
    top: -9px;
    height: 3px;
    background: var(--gold-pale);
  }
  .card--back .gold-band { height: 62px; }
  .card--front .gold-band { height: 90px; }

  .brand-name {
    position: absolute;
    left: 0;
    right: 0;
    text-align: center;
    font-family: "Tinos", "Times New Roman", serif;
    font-size: 34px;
    color: var(--gold-text);
    letter-spacing: 0.5px;
  }
  .tagline {
    position: absolute;
    left: 0;
    right: 0;
    text-align: center;
    font-family: "Arimo", Arial, sans-serif;
    font-weight: 700;
    font-size: 13px;
    color: var(--ink);
  }
  .card--back .brand-name { top: 108px; }
  .card--back .tagline { top: 152px; }

  .product-photo {
    position: absolute;
    left: 215px;
    top: 40px;
    width: 130px;
    height: 120px;
    border-radius: 50%;
    background: radial-gradient(circle at 45% 45%, var(--ring-tone-light) 0%, #cfcfcf 55%, var(--ring-tone-dark) 75%, rgba(255,255,255,0) 76%);
  }
  .card--front .brand-name { top: 168px; }
  .card--front .tagline { top: 212px; }

  .email {
    position: absolute;
    left: 150px;
    bottom: 46px;
    font-family: "Arimo", Arial, sans-serif;
    font-size: 15px;
    color: var(--band-text);
    letter-spacing: 0.2px;
  }
</style>
</head>
<body>
<main class="canvas">
  <section class="card card--back" aria-label="Card back">
    <h1 class="brand-name">Qvwtrading.net</h1>
    <p class="tagline">Known for our ideal fit rings</p>
    <div class="gold-band"></div>
  </section>

  <section class="card card--front" aria-label="Card front">
    <div class="product-photo" role="img" aria-label="Photo of two polished steel wedding rings"></div>
    <h2 class="brand-name">Qvwtrading.net</h2>
    <p class="tagline">Known for our ideal fit rings</p>
    <div class="gold-band"></div>
    <p class="email">email.marentullochptyltd@corvexmail com</p>
  </section>
</main>
</body>
</html>
```